Business Card Design Project

Hi I am after a business card double sided 1 side to have the attached PDF on front on the back:

Trent Malloway - Managing Director
Mobile: 0413 268 471
email: trent@vrixo.com.au
web: www.vrixo.com.au

Industry/Entity Type

Business

Font styles to use
Sans Serif

Requirements
Must have
• I want a classy looking card
Nice to have
• I like lime green and black and white

```html
<!DOCTYPE html>
<html lang="en">
<head>
<meta charset="utf-8">
<title>Trent Malloway – Business Card</title>
<link href="https://fonts.googleapis.com/css2?family=Poppins:wght@600;700&family=Questrial&display=swap" rel="stylesheet">
<style>
  :root {
    --lime: #add136;
    --ink: #111111;
    --paper: #ffffff;
    --slate: #8a8a8a;
    --band: #000000;
  }
  html, body {
    margin: 0;
    padding: 0;
    overflow: hidden;
    background: var(--paper);
  }
  .card {
    position: relative;
    width: 1200px;
    height: 667px;
    background: var(--paper);
    overflow: hidden;
    font-family: "Questrial", sans-serif;
  }
  .accent-top {
    position: absolute;
    left: 416px;
    top: 0;
    width: 112px;
    height: 278px;
    background: var(--lime);
  }
  .accent-spine {
    position: absolute;
    left: 596px;
    top: 206px;
    width: 116px;
    height: 378px;
    background: var(--lime);
  }
  .identity {
    position: absolute;
    right: 672px;
    top: 294px;
    text-align: right;
    white-space: nowrap;
  }
  .identity__name {
    margin: 0;
    font-family: "Poppins", sans-serif;
    font-weight: 600;
    font-size: 56px;
    line-height: 1;
    letter-spacing: -1.5px;
    color: var(--ink);
    text-transform: uppercase;
  }
  .identity__role {
    margin: 14px 2px 0 0;
    font-family: "Poppins", sans-serif;
    font-weight: 700;
    font-size: 27px;
    line-height: 1;
    color: var(--lime);
    text-transform: uppercase;
  }
  .contact {
    position: absolute;
    left: 589px;
    top: 211px;
    margin: 0;
    padding: 0;
    list-style: none;
  }
  .contact__item {
    display: flex;
    align-items: center;
    height: 66px;
    margin-bottom: 30px;
  }
  .contact__key {
    width: 131px;
    height: 66px;
    display: flex;
    align-items: center;
    justify-content: center;
    background: var(--slate);
    border-radius: 3px;
    box-shadow: 0 2px 6px rgba(0,0,0,0.35);
    color: var(--paper);
    font-family: "Poppins", sans-serif;
    font-weight: 700;
    font-size: 30px;
  }
  .contact__value {
    margin-left: 30px;
    font-size: 34px;
    color: var(--ink);
    white-space: nowrap;
  }
  .services {
    position: absolute;
    left: 0;
    bottom: 0;
    width: 1200px;
    height: 83px;
    background: var(--band);
    display: flex;
    align-items: center;
    justify-content: center;
    color: var(--paper);
    font-size: 35px;
    letter-spacing: 0.5px;
  }
  .services__item { padding: 0 26px; }
  .services__divider {
    width: 2px;
    height: 40px;
    background: var(--paper);
  }
</style>
</head>
<body>
  <div class="card">
    <div class="accent-top"></div>
    <div class="accent-spine"></div>

    <div class="identity">
      <h1 class="identity__name">Trent Malloway</h1>
      <p class="identity__role">Managing Director</p>
    </div>

    <ul class="contact">
      <li class="contact__item"><span class="contact__key">m</span><span class="contact__value">0413 268 471</span></li>
      <li class="contact__item"><span class="contact__key">e</span><span class="contact__value">trent@vrixo.com.au</span></li>
      <li class="contact__item"><span class="contact__key">w</span><span class="contact__value">www.vrixo.com.au</span></li>
    </ul>

    <div class="services">
      <span class="services__item">ORGANIZATION</span>
      <span class="services__divider"></span>
      <span class="services__item">PLANING</span>
      <span class="services__divider"></span>
      <span class="services__item">FINANCE</span>
      <span class="services__divider"></span>
      <span class="services__item">MANAGE</span>
    </div>
  </div>
</body>
</html>
```